meridale partners business card

Architectural firm business card
Updates

Please note:

corporate colour black+yellow are the only elements to be kept.
NO OTHER ELEMENT TO BE REUSED FROM PREVIOUS BUSINESS CARD.
Thank you.

Dear Everyone,

Thank you for your participation. I have upload the KBSO+ logo again for incoporate in the card. in tif and pdf format.

Thank you 

I keep getting request for the logo file. Does everyone has the same problem?

I cannot do much, because the file is upload to the website server. I can't seem to see it either.

The logo file is now working. Please download. I check it myself. Thank you everyone.

Dear All,

Thank you for all the hard work. There are a lot of great work. Due to current commitment with work, I am unable to review them just yet. I will do so next week and advise everyone also. Thank you again. Best regards

Dear All,

Thank you for your participation. There are a lot of good design. Unfortunately, I can only select one. All the best. This is definitely a good crowd to work with. Thank you everyone again.

Best regards

Target Market(s)

Corporate, commercial and institutional projects only

Industry/Entity Type

Business

Requirements
Must have
• elegant simple
double sided with coating
Member of Southland Guild of Draughtsmen (logo only)
corporate colour black and

LOGO FILE UPLOADED
Should not have
• should not be the same as current business card.
upload for reference information only.
font sans serif preferred.

```html
<!DOCTYPE html>
<html lang="en">
<head>
<meta charset="utf-8">
<title>meridale partners business card</title>
<link rel="stylesheet" href="https://fonts.googleapis.com/css2?family=Montserrat:wght@200;300;400;600&display=swap">
<style>
  :root {
    --brand-yellow: #f2ad4e;
    --brand-black: #0c0c0c;
    --paper-bg: #e4e4e2;
    --text-light: #ffffff;
    --text-grey: #bdbdbd;
    --badge-dark: #111111;
  }
  * { box-sizing: border-box; margin: 0; padding: 0; }
  html, body {
    width: 1200px; height: 900px; overflow: hidden;
    background: var(--paper-bg);
    font-family: "Montserrat", sans-serif;
  }
  .sheet {
    position: relative; width: 1200px; height: 900px;
    display: flex; flex-direction: column; align-items: center;
    justify-content: center; gap: 50px;
  }
  .card {
    position: relative; width: 620px; height: 378px;
    box-shadow: 0 6px 18px rgba(0,0,0,0.25);
  }
  .card--front { background: var(--brand-yellow); }
  .card--back { background: var(--brand-black); color: var(--text-light); }

  .services {
    position: absolute; top: 18px; right: 22px;
    text-align: right; font-weight: 300; font-size: 13px; line-height: 1.2;
    color: var(--text-light);
  }
  .card--back .services { color: var(--text-grey); }

  .member-badge {
    position: absolute; top: 22px; right: 150px;
    width: 118px; height: 48px; display: flex;
  }
  .member-badge__mark { width: 44px; height: 48px; background: var(--badge-dark); }
  .member-badge__panel { flex: 1; background: var(--text-light); border: 2px solid var(--badge-dark); }

  .wordmark {
    position: absolute; color: var(--text-light);
    font-weight: 200; white-space: nowrap;
  }
  .wordmark__name { font-size: 46px; letter-spacing: 1px; }
  .wordmark__suffix { font-size: 11px; font-weight: 400; margin-left: 8px; vertical-align: 14px; }
  .card--front .wordmark { left: 30px; bottom: 20px; }
  .card--back .wordmark { left: 34px; top: 90px; }
  .card--back .wordmark__name { font-size: 40px; }

  .divider {
    position: absolute; left: 340px; top: 180px;
    width: 1px; height: 170px; background: var(--text-light);
  }

  .contact-person {
    position: absolute; left: 60px; bottom: 40px;
    font-size: 15px; font-weight: 300; line-height: 1.3;
  }
  .contact-person__name { color: var(--brand-yellow); font-weight: 600; font-size: 21px; }
  .contact-person__cred { color: var(--text-light); font-weight: 300; font-size: 13px; }
  .contact-person__role { color: var(--brand-yellow); }
  .contact-person__mobile { margin-top: 8px; }

  .label { color: var(--brand-yellow); font-weight: 400; }

  .office {
    position: absolute; left: 370px; top: 180px;
    font-size: 14px; font-weight: 300; line-height: 1.3;
  }
  .office__address { color: var(--text-grey); margin-bottom: 36px; }
  .office__web { color: var(--brand-yellow); font-weight: 400; }
</style>
</head>
<body>
<main class="sheet">
  <section class="card card--front" aria-label="Card front">
    <div class="member-badge" role="img" aria-label="Member badge of the Southland Guild of Draughtsmen">
      <span class="member-badge__mark"></span>
      <span class="member-badge__panel"></span>
    </div>
    <p class="services">architects<br>urban designers<br>project managers</p>
    <p class="wordmark"><span class="wordmark__name">meridale</span><span class="wordmark__suffix">partners pty limited</span></p>
  </section>

  <section class="card card--back" aria-label="Card back">
    <p class="services">architects<br>urban designers<br>project managers</p>
    <p class="wordmark"><span class="wordmark__name">meridale</span><span class="wordmark__suffix">partners pty limited</span></p>
    <span class="divider"></span>

    <div class="contact-person">
      <p><span class="contact-person__name">Linh Carver</span> <span class="contact-person__cred">kbso, sgd</span></p>
      <p>Architect (NSW BoA reg. no. 7312)</p>
      <p class="contact-person__role">Director</p>
      <p class="contact-person__mobile"><span class="label">M.</span> 0400 12 45 78</p>
    </div>

    <div class="office">
      <p class="office__address">Corran House<br>18 Elwood Lane, Kelby Park<br>NSW 2190</p>
      <p><span class="label">T.</span> +612 9400 1257 &nbsp;<span class="label">F.</span> +612 9400 1258</p>
      <p><span class="label">E.</span> mail@meridalepartners.example</p>
      <p class="office__web">www.meridalepartners.example</p>
    </div>
  </section>
</main>
</body>
</html>
```